Cloudmarra label design 2.5 x 3.5 in size can go either way

need a label design created for a eliquid line called cloudmarra the line was called lanternfall but there are a few other companies out there going by the same name so we are trying to rebrand there is a company called tollgate brewing company and i really like the looks of all there boxes and labels so I want the label to resemble the style of there labels but be unique to us we have 7 flavors so each label can have the same basic layout but a different color for each name and flavor i will attach pictures of the old label and ideas for the new label we want to stick to a lanternfall era/ mobster kinda look the flavors are:
gusto
tinsel
moonharvest
cold snap
march 3rd
pinwheel
fig
I also attached some of our other lines pictures for reference as to how its gonna be used

Target Market(s)

Vapers

Colors

Requirements
Must have
• if you look at the lanternfall label I posted in the pictures it will show the things that have to be included
• Nicotine Content
• Made in USA
• ISO 7 certified
• cloudmarra name on top
• flavor name on bottom
• nicotine warning or space on side of label that I can add
Nice to have
• bold colors for the name and flavor rest in greyscale

```html
<!DOCTYPE html>
<html lang="en">
<head>
<meta charset="utf-8">
<title>Cloudmarra Ultra Premium Liquid – Label Line</title>
<link rel="stylesheet" href="https://fonts.googleapis.com/css2?family=Oswald:wght@300;400;600&family=Roboto+Condensed:wght@400;700&display=swap">
<style>
  :root {
    --page: #ffffff;
    --label-bg: #29292c;
    --label-bg-deep: #1d1d1f;
    --ink: #f2f2f2;
    --ink-soft: #c4c4c4;
    --ink-dim: #8a8a8a;
    --tinsel: #9d45c8;
    --coldsnap: #e3238d;
    --pinwheel: #e9c52c;
    --gusto: #e23c3c;
    --moonharvest: #f07b24;
    --fig: #2fa8e2;
    --march: #3cc04b;
  }
  * { box-sizing: border-box; margin: 0; padding: 0; }
  html, body { width: 1200px; height: 492px; overflow: hidden; background: var(--page); }
  .label-line {
    width: 1200px; height: 492px;
    display: flex; justify-content: center; align-items: flex-start; gap: 25px;
    padding-top: 168px;
  }
  .label {
    --accent: var(--tinsel);
    position: relative;
    width: 133px; height: 248px;
    background: linear-gradient(180deg, var(--label-bg) 0%, var(--label-bg-deep) 100%);
    color: var(--ink);
    display: flex; flex-direction: column; align-items: center;
    padding: 6px 7px 6px;
    font-family: "Roboto Condensed", sans-serif;
    overflow: hidden;
  }
  .label::before {
    content: ""; position: absolute; inset: 3px;
    border: 1px solid var(--accent); opacity: .8; pointer-events: none;
  }
  .label--tinsel { --accent: var(--tinsel); }
  .label--coldsnap { --accent: var(--coldsnap); }
  .label--pinwheel { --accent: var(--pinwheel); }
  .label--gusto { --accent: var(--gusto); }
  .label--moonharvest { --accent: var(--moonharvest); }
  .label--fig { --accent: var(--fig); }
  .label--march { --accent: var(--march); }

  .brand-mark { display: flex; align-items: center; gap: 3px; height: 18px; }
  .brand-mark__dot { width: 12px; height: 12px; border-radius: 50%; border: 1.5px solid var(--ink); }
  .brand-mark__name { font-weight: 700; font-size: 6px; letter-spacing: 1px; color: var(--ink); }

  .wordmark {
    font-family: "Oswald", sans-serif; font-weight: 600;
    font-size: 21px; line-height: 1; letter-spacing: .2px;
    color: var(--ink); margin-top: 2px; text-transform: uppercase;
  }
  .tagline { font-size: 4.6px; letter-spacing: .6px; color: var(--ink-soft); margin-top: 1px; text-transform: uppercase; }

  .flavor-banner { position: relative; width: 116px; height: 26px; margin-top: 4px; display: flex; align-items: center; justify-content: center; }
  .flavor-banner svg { position: absolute; inset: 0; width: 100%; height: 100%; }
  .flavor-banner__frame { fill: none; stroke: var(--accent); stroke-width: 1.1; }
  .flavor-banner__inner { fill: none; stroke: var(--accent); stroke-width: .5; opacity: .6; }
  .flavor-name {
    position: relative; font-family: "Oswald", sans-serif; font-weight: 400; font-size: 15px; line-height: 1;
    color: var(--ink); white-space: nowrap; text-transform: uppercase;
  }
  .flavor-name--long { font-size: 12.5px; }

  .rule { width: 96px; height: 1px; background: var(--accent); opacity: .7; margin-top: 4px; }
  .flavor-notes { font-size: 5.6px; letter-spacing: .3px; color: var(--ink); margin-top: 3px; text-transform: uppercase; white-space: nowrap; }
  .volume { font-family: "Oswald", sans-serif; font-size: 6.5px; letter-spacing: .8px; color: var(--ink-soft); margin-top: 3px; }

  .seal-row { position: relative; width: 118px; height: 30px; margin-top: 2px; display: flex; align-items: center; justify-content: space-between; }
  .seal-row__ornament {
    position: absolute; left: 24px; right: 24px; top: 3px; bottom: 3px;
    background: radial-gradient(ellipse at center, color-mix(in srgb, var(--accent) 40%, transparent) 0%, transparent 75%);
  }
  .seal { position: relative; display: flex; flex-direction: column; align-items: center; gap: 1px; width: 24px; }
  .seal__disc { width: 20px; height: 20px; border-radius: 50%; background: var(--accent); border: 1.5px solid var(--label-bg-deep); box-shadow: 0 0 0 1px var(--accent); }
  .seal__caption { font-size: 4.4px; font-weight: 700; letter-spacing: .4px; color: var(--ink); text-transform: uppercase; white-space: nowrap; }

  .warning-title { font-size: 5px; letter-spacing: .8px; color: var(--ink-soft); margin-top: 2px; text-transform: uppercase; border-top: 1px solid var(--ink-dim); padding-top: 2px; width: 108px; text-align: center; }
  .warning-text { font-size: 4.5px; line-height: 1.2; color: var(--ink-soft); margin-top: 2px; width: 117px; text-align: justify; }
</style>
</head>
<body>
<main class="label-line">

  <article class="label label--tinsel">
    <div class="brand-mark"><span class="brand-mark__dot"></span><span class="brand-mark__name">CLOUDMARRA</span></div>
    <h2 class="wordmark">Cloudmarra</h2>
    <p class="tagline">Ultra Premium Liquid</p>
    <div class="flavor-banner"><svg viewBox="0 0 116 26" preserveAspectRatio="none" aria-hidden="true"><polygon class="flavor-banner__frame" points="9,1 107,1 115,13 107,25 9,25 1,13"/><polygon class="flavor-banner__inner" points="11,3.5 105,3.5 112,13 105,22.5 11,22.5 4,13"/></svg><span class="flavor-name">Tinsel</span></div>
    <div class="rule"></div>
    <p class="flavor-notes">Gooey Butter Cake</p>
    <p class="volume">120 ML</p>
    <div class="seal-row"><div class="seal"><span class="seal__disc"></span><span class="seal__caption">Made in USA</span></div><div class="seal-row__ornament" role="img" aria-label="Decorative filigree ornament"></div><div class="seal"><span class="seal__disc"></span><span class="seal__caption">ISO 7</span></div></div>
    <p class="warning-title">Nicotine Warning</p>
    <p class="warning-text">The products offered by Cloudmarra are intended for use by responsible adult users over the age of 18 (or the legal smoking age of your state), and are not intended for use by minors, women who are pregnant or breastfeeding, or persons with or at risk of heart disease, high blood pressure, diabetes, asthma, or those who are sensitive to nicotine or propylene glycol. Nicotine is highly addictive and habit forming. Keep out of reach of children and pets. Some of our products contain nicotine, a chemical known to the State of California to cause birth defects or other reproductive harm.</p>
  </article>

  <article class="label label--coldsnap">
    <div class="brand-mark"><span class="brand-mark__dot"></span><span class="brand-mark__name">CLOUDMARRA</span></div>
    <h2 class="wordmark">Cloudmarra</h2>
    <p class="tagline">Ultra Premium Liquid</p>
    <div class="flavor-banner"><svg viewBox="0 0 116 26" preserveAspectRatio="none" aria-hidden="true"><polygon class="flavor-banner__frame" points="9,1 107,1 115,13 107,25 9,25 1,13"/><polygon class="flavor-banner__inner" points="11,3.5 105,3.5 112,13 105,22.5 11,22.5 4,13"/></svg><span class="flavor-name">Cold Snap</span></div>
    <div class="rule"></div>
    <p class="flavor-notes">Strawberry Fruit Chew</p>
    <p class="volume">120 ML</p>
    <div class="seal-row"><div class="seal"><span class="seal__disc"></span><span class="seal__caption">Made in USA</span></div><div class="seal-row__ornament" role="img" aria-label="Decorative filigree ornament"></div><div class="seal"><span class="seal__disc"></span><span class="seal__caption">ISO 7</span></div></div>
    <p class="warning-title">Nicotine Warning</p>
    <p class="warning-text">The products offered by Cloudmarra are intended for use by responsible adult users over the age of 18 (or the legal smoking age of your state), and are not intended for use by minors, women who are pregnant or breastfeeding, or persons with or at risk of heart disease, high blood pressure, diabetes, asthma, or those who are sensitive to nicotine or propylene glycol. Nicotine is highly addictive and habit forming. Keep out of reach of children and pets. Some of our products contain nicotine, a chemical known to the State of California to cause birth defects or other reproductive harm.</p>
  </article>

  <article class="label label--pinwheel">
    <div class="brand-mark"><span class="brand-mark__dot"></span><span class="brand-mark__name">CLOUDMARRA</span></div>
    <h2 class="wordmark">Cloudmarra</h2>
    <p class="tagline">Ultra Premium Liquid</p>
    <div class="flavor-banner"><svg viewBox="0 0 116 26" preserveAspectRatio="none" aria-hidden="true"><polygon class="flavor-banner__frame" points="9,1 107,1 115,13 107,25 9,25 1,13"/><polygon class="flavor-banner__inner" points="11,3.5 105,3.5 112,13 105,22.5 11,22.5 4,13"/></svg><span class="flavor-name">Pinwheel</span></div>
    <div class="rule"></div>
    <p class="flavor-notes">Butterscotch Custard</p>
    <p class="volume">120 ML</p>
    <div class="seal-row"><div class="seal"><span class="seal__disc"></span><span class="seal__caption">Made in USA</span></div><div class="seal-row__ornament" role="img" aria-label="Decorative filigree ornament"></div><div class="seal"><span class="seal__disc"></span><span class="seal__caption">ISO 7</span></div></div>
    <p class="warning-title">Nicotine Warning</p>
    <p class="warning-text">The products offered by Cloudmarra are intended for use by responsible adult users over the age of 18 (or the legal smoking age of your state), and are not intended for use by minors, women who are pregnant or breastfeeding, or persons with or at risk of heart disease, high blood pressure, diabetes, asthma, or those who are sensitive to nicotine or propylene glycol. Nicotine is highly addictive and habit forming. Keep out of reach of children and pets. Some of our products contain nicotine, a chemical known to the State of California to cause birth defects or other reproductive harm.</p>
  </article>

  <article class="label label--gusto">
    <div class="brand-mark"><span class="brand-mark__dot"></span><span class="brand-mark__name">CLOUDMARRA</span></div>
    <h2 class="wordmark">Cloudmarra</h2>
    <p class="tagline">Ultra Premium Liquid</p>
    <div class="flavor-banner"><svg viewBox="0 0 116 26" preserveAspectRatio="none" aria-hidden="true"><polygon class="flavor-banner__frame" points="9,1 107,1 115,13 107,25 9,25 1,13"/><polygon class="flavor-banner__inner" points="11,3.5 105,3.5 112,13 105,22.5 11,22.5 4,13"/></svg><span class="flavor-name">Gusto</span></div>
    <div class="rule"></div>
    <p class="flavor-notes">Caramel Apple</p>
    <p class="volume">120 ML</p>
    <div class="seal-row"><div class="seal"><span class="seal__disc"></span><span class="seal__caption">Made in USA</span></div><div class="seal-row__ornament" role="img" aria-label="Decorative filigree ornament"></div><div class="seal"><span class="seal__disc"></span><span class="seal__caption">ISO 7</span></div></div>
    <p class="warning-title">Nicotine Warning</p>
    <p class="warning-text">The products offered by Cloudmarra are intended for use by responsible adult users over the age of 18 (or the legal smoking age of your state), and are not intended for use by minors, women who are pregnant or breastfeeding, or persons with or at risk of heart disease, high blood pressure, diabetes, asthma, or those who are sensitive to nicotine or propylene glycol. Nicotine is highly addictive and habit forming. Keep out of reach of children and pets. Some of our products contain nicotine, a chemical known to the State of California to cause birth defects or other reproductive harm.</p>
  </article>

  <article class="label label--moonharvest">
    <div class="brand-mark"><span class="brand-mark__dot"></span><span class="brand-mark__name">CLOUDMARRA</span></div>
    <h2 class="wordmark">Cloudmarra</h2>
    <p class="tagline">Ultra Premium Liquid</p>
    <div class="flavor-banner"><svg viewBox="0 0 116 26" preserveAspectRatio="none" aria-hidden="true"><polygon class="flavor-banner__frame" points="9,1 107,1 115,13 107,25 9,25 1,13"/><polygon class="flavor-banner__inner" points="11,3.5 105,3.5 112,13 105,22.5 11,22.5 4,13"/></svg><span class="flavor-name flavor-name--long">Moonharvest</span></div>
    <div class="rule"></div>
    <p class="flavor-notes">Pineapple, Strawberry, Pina Colada</p>
    <p class="volume">120 ML</p>
    <div class="seal-row"><div class="seal"><span class="seal__disc"></span><span class="seal__caption">Made in USA</span></div><div class="seal-row__ornament" role="img" aria-label="Decorative filigree ornament"></div><div class="seal"><span class="seal__disc"></span><span class="seal__caption">ISO 7</span></div></div>
    <p class="warning-title">Nicotine Warning</p>
    <p class="warning-text">The products offered by Cloudmarra are intended for use by responsible adult users over the age of 18 (or the legal smoking age of your state), and are not intended for use by minors, women who are pregnant or breastfeeding, or persons with or at risk of heart disease, high blood pressure, diabetes, asthma, or those who are sensitive to nicotine or propylene glycol. Nicotine is highly addictive and habit forming. Keep out of reach of children and pets. Some of our products contain nicotine, a chemical known to the State of California to cause birth defects or other reproductive harm.</p>
  </article>

  <article class="label label--fig">
    <div class="brand-mark"><span class="brand-mark__dot"></span><span class="brand-mark__name">CLOUDMARRA</span></div>
    <h2 class="wordmark">Cloudmarra</h2>
    <p class="tagline">Ultra Premium Liquid</p>
    <div class="flavor-banner"><svg viewBox="0 0 116 26" preserveAspectRatio="none" aria-hidden="true"><polygon class="flavor-banner__frame" points="9,1 107,1 115,13 107,25 9,25 1,13"/><polygon class="flavor-banner__inner" points="11,3.5 105,3.5 112,13 105,22.5 11,22.5 4,13"/></svg><span class="flavor-name">Fig</span></div>
    <div class="rule"></div>
    <p class="flavor-notes">Mixed Berries and Cream</p>
    <p class="volume">120 ML</p>
    <div class="seal-row"><div class="seal"><span class="seal__disc"></span><span class="seal__caption">Made in USA</span></div><div class="seal-row__ornament" role="img" aria-label="Decorative filigree ornament"></div><div class="seal"><span class="seal__disc"></span><span class="seal__caption">ISO 7</span></div></div>
    <p class="warning-title">Nicotine Warning</p>
    <p class="warning-text">The products offered by Cloudmarra are intended for use by responsible adult users over the age of 18 (or the legal smoking age of your state), and are not intended for use by minors, women who are pregnant or breastfeeding, or persons with or at risk of heart disease, high blood pressure, diabetes, asthma, or those who are sensitive to nicotine or propylene glycol. Nicotine is highly addictive and habit forming. Keep out of reach of children and pets. Some of our products contain nicotine, a chemical known to the State of California to cause birth defects or other reproductive harm.</p>
  </article>

  <article class="label label--march">
    <div class="brand-mark"><span class="brand-mark__dot"></span><span class="brand-mark__name">CLOUDMARRA</span></div>
    <h2 class="wordmark">Cloudmarra</h2>
    <p class="tagline">Ultra Premium Liquid</p>
    <div class="flavor-banner"><svg viewBox="0 0 116 26" preserveAspectRatio="none" aria-hidden="true"><polygon class="flavor-banner__frame" points="9,1 107,1 115,13 107,25 9,25 1,13"/><polygon class="flavor-banner__inner" points="11,3.5 105,3.5 112,13 105,22.5 11,22.5 4,13"/></svg><span class="flavor-name">March 3rd</span></div>
    <div class="rule"></div>
    <p class="flavor-notes">Berry Lemon Lime</p>
    <p class="volume">120 ML</p>
    <div class="seal-row"><div class="seal"><span class="seal__disc"></span><span class="seal__caption">Made in USA</span></div><div class="seal-row__ornament" role="img" aria-label="Decorative filigree ornament"></div><div class="seal"><span class="seal__disc"></span><span class="seal__caption">ISO 7</span></div></div>
    <p class="warning-title">Nicotine Warning</p>
    <p class="warning-text">The products offered by Cloudmarra are intended for use by responsible adult users over the age of 18 (or the legal smoking age of your state), and are not intended for use by minors, women who are pregnant or breastfeeding, or persons with or at risk of heart disease, high blood pressure, diabetes, asthma, or those who are sensitive to nicotine or propylene glycol. Nicotine is highly addictive and habit forming. Keep out of reach of children and pets. Some of our products contain nicotine, a chemical known to the State of California to cause birth defects or other reproductive harm.</p>
  </article>

</main>
</body>
</html>
```